Website design for an edge protection barrier system

- The design must be based around the attached HPID (home page information design) called CODE HPID. I've attached Word and PDF versions - these are the same. The table boxes are just for approximate placement of information – you DON'T have to make it look exactly like this. All fonts used in the HPID are only examples - you can use any Google font you wish.

- Information only is in orange text. Copy to go on the design in black text. Some instructions are in the HPID. Please be creative!

- The design needs to be modern. Colours are to be black and white with orange ...like the logo colours.

- I've provided the images for the galleries - they are labelled and will match the name in the HPID.

- Examples of some websites that have great design... don't copy them please but they are similar in look to what we are after....
http://wandertrail.co.nz/
http://www.lumfuel.co.nz/
http://www.tolbertwade.co.nz/

Width of content will be 1100 pixels when implemented as a web page. Header height (without nav bar) 150-160 pixels.

If your design is chosen the winning PSD file will have to be provided as follows…
1. Canvas size of 2000px x 2000px - 72ppi in Adobe Photoshop (CS5 compatible)
2. Width of content section is 1100px wide - centered in the canvas
3. Any button rollovers/hovers in the PSD as hidden layers.
4. All fonts used must be Google fonts (except for the fonts in the header at the top of the page).
5. You will need to supply the chosen home page plus one example page (example page as a style guide for how all other pages will look). Example page is only the header and navigational bar at the top, an empty sector in the middle with a column (180 px wide) which can be left or right aligned which means the main sector is 920 pixels wide, and then the footer at the bottom of the page
Updates

Hi all, As per the HPID for the main image gallery you must use: File 7: edge protection systems for new houses hp wednesday, 17 december 2014 04:35:4112 AND File 9: e bracket for new home edge protection hp wednesday, 17 december 2014 04:35:4111 Use these images so they fit next to each other with the words: Edge protection systems for new houses with timber or aluminium rails (These words must be used either on or above or below the gallery) What we are looking for is a clean modern layout of the home page. The images supplied must be used please. Thank you.

Our office is closed over the New Year holiday season so decisions on designs may be delayed.

```html
<!DOCTYPE html>
<html lang="en">
<head>
<meta charset="utf-8">
<title>Ridgeline Guard – Edge Protection Systems</title>
<link href="https://fonts.googleapis.com/css2?family=Open+Sans:wght@400;600;700&display=swap" rel="stylesheet">
<style>
:root{
  --orange:#f29a1f;
  --dark:#1f1f1f;
  --darker:#151515;
  --page:#ececec;
  --panel:#ffffff;
  --text:#3d3d3d;
  --body:#555;
  --rule:#d6d6d6;
  --foot-text:#c8c8c8;
}
*{box-sizing:border-box;margin:0;padding:0}
html,body{width:882px;height:1200px;overflow:hidden}
body{background:var(--page);font-family:"Open Sans",Arial,sans-serif;color:var(--text);font-size:8px;line-height:1.5;display:flex;flex-direction:column}
.wrap{width:650px;margin:0 auto}
.site-header{background:var(--dark);height:30px;flex:none}
.site-header .wrap{display:flex;align-items:center;height:30px;position:relative}
.phone{position:absolute;left:-14px;top:3px;color:var(--orange);font-size:5.5px;font-weight:600}
.brand{display:flex;align-items:center;gap:5px;color:var(--orange);font-weight:700;font-size:12px;margin-left:-14px;margin-top:8px}
.brand .mark{width:10px;height:10px;background:var(--orange)}
.nav{margin-left:auto;display:flex;gap:2px}
.nav a{color:#e0e0e0;text-decoration:none;font-size:6.5px;padding:4px 7px}
.nav a.active{background:var(--orange);color:#fff}
main{flex:none}
.hero{margin-top:8px;display:grid;grid-template-columns:1fr 1fr;gap:4px;height:164px;background:var(--panel);padding:4px 4px 0}
.hero .shot{background:linear-gradient(180deg,#8db7dc 0%,#c9dcea 40%,#b78b5c 70%,#6d5a46 100%)}
.hero .shot.b{background:linear-gradient(180deg,#9cc1e0 0%,#d3e2ee 45%,#c69a66 72%,#5e4d3c 100%)}
.hero-caption{background:var(--darker);color:var(--orange);text-align:center;font-weight:700;font-size:7px;padding:5px 0;letter-spacing:.3px;text-transform:uppercase}
.content{background:var(--panel);padding:14px 22px 10px}
.grid{display:grid;grid-template-columns:repeat(3,1fr);gap:16px 14px}
.tile h3{color:var(--orange);font-size:8px;font-weight:600;margin-bottom:4px}
.tile .photo{height:70px;background:linear-gradient(135deg,#9fb3c4,#6f7d86);position:relative}
.tile .photo.soon{background:linear-gradient(135deg,#9a9a9a,#6a6a6a)}
.tile .photo.soon span{position:absolute;inset:0;display:flex;align-items:center;justify-content:center;color:#fff;font-size:10px}
.tile .more{background:var(--orange);color:#fff;text-align:center;font-size:6.5px;padding:2px 0}
p{font-size:7.5px;color:var(--body);margin-bottom:5px}
.intro{margin-top:14px}
.btn{display:inline-block;background:var(--orange);color:#fff;font-size:6.5px;padding:3px 14px;margin-top:4px}
hr.rule{border:0;border-top:1px solid var(--rule);margin:16px 0 12px}
.two-col{display:flex;gap:24px}
.two-col>div{flex:1}
h2{color:var(--orange);font-size:11px;font-weight:600;margin-bottom:3px}
.video{height:130px;margin-top:4px;background:linear-gradient(135deg,#e6e6e6,#c9c9c9);position:relative}
.video svg{position:absolute;left:50%;top:50%;transform:translate(-50%,-50%)}
.testimonial{display:flex;gap:20px}
.testimonial .photo{width:150px;height:105px;flex:none;background:linear-gradient(180deg,#bcd0df,#8a7058)}
.testimonial .who{color:var(--orange);font-weight:600}
.site-footer{background:var(--dark);color:var(--foot-text);padding:16px 0 0;margin-top:12px;flex:1}
.footer-cols{display:flex;gap:24px;padding:0 22px}
.footer-cols>div{flex:1}
.footer-cols h4{color:var(--orange);font-size:8px;font-weight:600;margin-bottom:5px}
.footer-cols li{list-style:none;font-size:7px;line-height:1.75}
.footer-cols p{color:var(--foot-text);font-size:7px}
.badge{display:flex;align-items:center;gap:6px;margin-top:6px;font-size:7px}
.badge i{width:14px;height:14px;background:#444;display:block}
.bottom-bar{background:var(--darker);margin-top:20px;padding:8px 22px;display:flex;gap:40px;font-size:7px;color:var(--foot-text)}
</style>
</head>
<body>
<header class="site-header">
  <div class="wrap">
    <span class="phone">0800 555 014</span>
    <div class="brand"><span class="mark"></span>Ridgeline Guard</div>
    <nav class="nav">
      <a class="active">Home</a><a>About Us</a><a>Edge Protection Systems</a><a>Video</a><a>Testimonials</a><a>Gallery</a><a>Contact</a>
    </nav>
  </div>
</header>

<main class="wrap">
  <div class="hero">
    <div class="shot" role="img" aria-label="Timber house frame with edge protection rails"></div>
    <div class="shot b" role="img" aria-label="E-bracket fitted for new home edge protection"></div>
  </div>
  <div class="hero-caption">Edge protection systems for new houses with timber or aluminium rails</div>

  <section class="content">
    <div class="grid">
      <div class="tile"><h3>New Build Soffit Return</h3><div class="photo" role="img" aria-label="Soffit return edge protection on a new build"></div><div class="more">more</div></div>
      <div class="tile"><h3>New Build Truss Return</h3><div class="photo" role="img" aria-label="Truss return edge protection on a new build"></div><div class="more">more</div></div>
      <div class="tile"><h3>Re-roof</h3><div class="photo" role="img" aria-label="Edge protection on a re-roofing job"></div><div class="more">more</div></div>
      <div class="tile"><h3>Garage and Shed</h3><div class="photo" role="img" aria-label="Edge protection around a garage roof"></div><div class="more">more</div></div>
      <div class="tile"><h3>Commercial</h3><div class="photo soon"><span>Coming soon</span></div><div class="more">more</div></div>
      <div class="tile"><h3>New Product</h3><div class="photo soon"><span>Coming soon</span></div><div class="more">more</div></div>
    </div>
    <p class="intro">Our edge protection rails fit timber or aluminium systems and set up quickly on new builds, re-roofs and garages. Every system is tested to meet safety standards, giving builders a secure working edge from frame to finish across every stage of the job.</p>
    <span class="btn">more</span>

    <hr class="rule">

    <div class="two-col">
      <div>
        <h2>Video</h2>
        <p>Watch the video to see the edge protection system at work.</p>
        <div class="video" role="img" aria-label="Video still of an edge protection bracket">
          <svg width="44" height="44" viewBox="0 0 44 44"><rect width="44" height="44" rx="6" fill="#222" opacity=".8"/><polygon points="17,12 32,22 17,32" fill="#fff"/></svg>
        </div>
      </div>
      <div>
        <h2>Edge Protection Systems</h2>
        <p>Ridgeline Guard is a local family business focused on building safety at height. Our systems are designed and manufactured here to suit residential builds.</p>
        <p>The system is simple to install and can be used with either timber or aluminium rails, making it flexible for builders on every type of site.</p>
        <p>Brackets are designed for fast setup and removal, lowering labour time while keeping workers safe.</p>
        <span class="btn">more</span>
      </div>
    </div>

    <hr class="rule">

    <h2>Testimonials</h2>
    <div class="testimonial">
      <div class="photo" role="img" aria-label="Completed house framed with edge protection rails"></div>
      <div>
        <p>"I would recommend Ridgeline Guard to any builder. The team delivered on time, the rails went up fast and the whole crew felt safe working on the roof edge. Great service from start to finish and a product we will keep using on every new house we build this year."</p>
        <p class="who">Mara Henson, Builder</p>
      </div>
    </div>
  </section>
</main>

<footer class="site-footer">
  <div class="wrap">
    <div class="footer-cols">
      <div><h4>Useful links</h4><ul><li>Home</li><li>About Us</li><li>Video</li><li>Testimonials</li><li>Gallery</li><li>Contact</li></ul></div>
      <div><h4>Edge Protection Systems</h4><ul><li>New Build Soffit Return</li><li>New Build Truss Return</li><li>Re-roof</li><li>Garage and Shed</li><li>Commercial</li><li>New Product</li></ul></div>
      <div><h4>Family NZ Owned Business</h4><p>Locally owned and operated, supplying builders across the region with safe edge systems.</p><div class="badge"><i></i>Proudly New Zealand Made</div></div>
    </div>
    <div class="bottom-bar"><span>0800 555 014</span><span>info@ridgelineguard.co.nz</span></div>
  </div>
</footer>
</body>
</html>
```